Motivational Poster Series for Students at Truck Driving School

We are looking for a series of 3 motivational posters (18"X 24") to be used in classrooms at a truck driving school. The audience for the posters will be the students that are currently in school and the purpose of the posters is to be motivational pieces that will be displayed on the walls.

We have provided the quotes below that are to be used on each poster. We have also provided some example images from PixVaultImages to give an idea on the backgrounds that we'd like to see on each poster. The images do not have to be exact, these are just examples of what we think will look good for each quote. Since this is a series, they can all be somewhat similar in look/feel - just with different images and quotes.

So, the basic idea is a background image/design with a quote being the main point of emphasis. Other than that, we would like to include the logo provided at a small scale in one of the corners of the poster as a watermark for branding purposes.

Below are the quotes for each of the 3 posters:

Poster 1 - “It’s very difficult to follow our dreams, but it’s even more difficult to forget them.” - Devan Okafor

Poster 2 - “Success doesn’t just come and find you, you have to go out and get it.” - Unknown

Poster 3 - “If you are not willing to learn, no one can help you. If you are determined to learn, no one can stop you.”
- Unknown

NOTE: these posters should be designed as 18" X 24" in size with 2 of them being landscape and one being portrait orientation (as shown in images provided below)

Below are some sample images to give an idea on what could be used as background design for each quote. The logo that should be used as a watermark in a corner for some subtle branding has been provided as well.

Target Market(s)

The target market for this series are truck drivers between the ages of 25-55. Mostly males.

Industry/Entity Type

Landscape

Requirements
Must have
• Quote featured, high quality background design/image, logo watermark

```html
<!DOCTYPE html>
<html lang="en">
<head>
<meta charset="utf-8">
<title>Motivational Poster – Determined to Learn</title>
<link href="https://fonts.googleapis.com/css2?family=Open+Sans:ital,wght@0,400;0,700;0,800;1,800&display=swap" rel="stylesheet">
<style>
  :root {
    --sky-top: #56616c;
    --sky-mid: #3b526f;
    --sky-blue: #1f43a3;
    --foliage: #b0632c;
    --grass: #7d7040;
    --road: #3b3733;
    --road-near: #4f4239;
    --quote-text: rgba(255, 255, 255, 0.86);
    --quote-mark: rgba(200, 200, 200, 0.7);
    --brand-text: rgba(255, 255, 255, 0.9);
    --brand-chip: rgba(120, 120, 120, 0.55);
  }
  html, body {
    margin: 0;
    padding: 0;
    overflow: hidden;
    background: #ffffff;
  }
  .poster {
    position: relative;
    width: 900px;
    height: 1200px;
    overflow: hidden;
    font-family: "Open Sans", Arial, sans-serif;
  }
  .poster__backdrop {
    position: absolute;
    inset: 0;
    background: linear-gradient(180deg,
      var(--sky-top) 0%,
      var(--sky-mid) 30%,
      var(--sky-blue) 50%,
      var(--foliage) 55%,
      var(--grass) 61%,
      var(--road) 72%,
      var(--road-near) 100%);
  }
  .poster__type {
    position: absolute;
    inset: 0;
  }
  .quote-line {
    fill: var(--quote-text);
    font-weight: 800;
  }
  .quote-line--italic { font-style: italic; }
  .quote-mark {
    fill: var(--quote-mark);
    font-weight: 800;
  }
  .quote-author {
    fill: var(--quote-text);
    font-weight: 400;
  }
  .brand {
    position: absolute;
    left: 20px;
    top: 1112px;
    width: 262px;
    height: 68px;
    display: flex;
    align-items: center;
    gap: 10px;
    padding: 0 10px;
    box-sizing: border-box;
    background: var(--brand-chip);
  }
  .brand__square {
    width: 40px;
    height: 40px;
    background: var(--brand-text);
    flex: none;
  }
  .brand__name {
    color: var(--brand-text);
    font-weight: 700;
    font-size: 19px;
    line-height: 1.05;
  }
</style>
</head>
<body>
  <main class="poster">
    <div class="poster__backdrop" role="img" aria-label="Photograph of an empty two-lane highway with a double yellow centre line, running through autumn woods toward the horizon under a dark stormy sky"></div>

    <svg class="poster__type" width="900" height="1200" viewBox="0 0 900 1200" xmlns="http://www.w3.org/2000/svg">
      <text class="quote-mark" x="0" y="250" font-size="230">“</text>
      <text class="quote-mark" x="760" y="1000" font-size="230">”</text>

      <text class="quote-line" x="12" y="180" font-size="112" textLength="870" lengthAdjust="spacingAndGlyphs">If you are not</text>
      <text class="quote-line" x="12" y="300" font-size="104" textLength="870" lengthAdjust="spacingAndGlyphs">willing to learn,</text>
      <text class="quote-line" x="12" y="414" font-size="96" textLength="886" lengthAdjust="spacingAndGlyphs">no one can help you.</text>
      <text class="quote-line" x="10" y="632" font-size="212" textLength="878" lengthAdjust="spacingAndGlyphs">If you are</text>
      <text class="quote-line" x="6" y="756" font-size="106" textLength="888" lengthAdjust="spacingAndGlyphs">determined to learn,</text>
      <text class="quote-line quote-line--italic" x="12" y="888" font-size="98" textLength="886" lengthAdjust="spacingAndGlyphs">no one can stop you.</text>

      <text class="quote-author" x="876" y="1014" font-size="46" text-anchor="end">-Unknown</text>
    </svg>

    <div class="brand">
      <span class="brand__square"></span>
      <span class="brand__name">Northway Driver Academy</span>
    </div>
  </main>
</body>
</html>
```